Business Card

We are looking to re-create our business card. Attached is the company logo. we would like it to be back and front. for example one side with the persons information and the other side with the company logo. Be as creative as you would like but also keep in mind, we are a Health Insurance company and we need to look professional as well.
Industry/Entity Type
Business

```html
<!DOCTYPE html>
<html lang="en">
<head>
<meta charset="utf-8">
<title>Crestline Health Partners — Business Card</title>
<link href="https://fonts.googleapis.com/css2?family=Source+Sans+3:wght@400;600;700&display=swap" rel="stylesheet">
<style>
  :root {
    --page: #eceef0;
    --card: #ffffff;
    --brand-blue: #4383bf;
    --brand-grey: #808285;
    --band-text: #ffffff;
    --shadow: rgba(40, 50, 60, 0.12);
  }
  * { box-sizing: border-box; margin: 0; padding: 0; }
  html, body {
    width: 1200px; height: 720px; overflow: hidden;
    background: var(--page);
    font-family: "Source Sans 3", "Myriad Pro", sans-serif;
  }
  .canvas {
    position: relative; width: 1200px; height: 720px;
    display: flex; align-items: center; justify-content: center; gap: 60px;
  }
  .card {
    position: relative; width: 525px; height: 300px;
    background: var(--card);
    box-shadow: 0 6px 22px var(--shadow);
    overflow: hidden;
  }
  /* Front: agent details */
  .card-front .identity {
    position: absolute; left: 0; top: 0; width: 100%; height: 150px;
    display: flex; flex-direction: column; align-items: center; justify-content: flex-end;
    padding-bottom: 18px;
  }
  .brand-square {
    width: 22px; height: 22px; background: var(--brand-blue); margin-bottom: 12px;
  }
  .agent-name {
    color: var(--brand-blue); font-weight: 700; font-size: 34px;
    letter-spacing: 0.5px; line-height: 1;
  }
  .agent-title {
    color: var(--brand-grey); font-weight: 400; font-size: 17px;
    letter-spacing: 1px; margin-top: 4px;
  }
  .contact-band {
    position: absolute; left: 0; bottom: 0; width: 100%; height: 150px;
    background: var(--brand-blue); color: var(--band-text);
    font-size: 15px; line-height: 1.35;
  }
  .contact-direct { position: absolute; left: 26px; bottom: 24px; }
  .contact-office { position: absolute; right: 26px; top: 22px; text-align: right; }
  /* Back: company name */
  .card-back {
    display: flex; align-items: center; justify-content: center; gap: 16px;
  }
  .company-name {
    color: var(--brand-blue); font-weight: 400; font-size: 36px; letter-spacing: 0.3px;
  }
  .card-back .brand-square { margin-bottom: 0; width: 26px; height: 26px; }
</style>
</head>
<body>
  <main class="canvas">
    <section class="card card-front" aria-label="Card front">
      <div class="identity">
        <div class="brand-square"></div>
        <h1 class="agent-name">DANA R. WHITFIELD</h1>
        <p class="agent-title">INSURANCE AGENT</p>
      </div>
      <div class="contact-band">
        <p class="contact-office">48 Linden Avenue, Brookfield, AL 35090<br>www.crestlinehp.com</p>
        <p class="contact-direct">555-014-2290<br>danawhitfield@crestlinehp.com</p>
      </div>
    </section>
    <section class="card card-back" aria-label="Card back">
      <div class="brand-square"></div>
      <h2 class="company-name">Crestline Health Partners</h2>
    </section>
  </main>
</body>
</html>
```